Hollow-Lanterns charity auctions

We need a three part design for a nonprofit charity auction platform. This platform will eventually interface with a cell phone app, therefore the initial design needs to be responsive. Each phase should produce a working web page that builds upon the previous phase. The first phase is strictly to be a content page which can present our YouTube channel. It should also be a direct link between our alternate social media resources, e.g. FB, Twitter, Instagram etc. We can afford $500 for each phase (total $1500). Only serious long-term designers need respond.

Target Market(s)

High profile celebrities
International Bidders
Social Media

Industry/Entity Type

Cell Phone

Number of Pages Required

5+ page

Requirements
Must have
• Logos
• Responsive between desktop and cell phone website
• Upgradeable
• Hyper text
• Blog
• Flash (with video and image storage) i.e. YouTube, Instagram, Pinterest etc.
• Background music
Nice to have
• Intuitive with action buttons e.g. automatic post buttons, play buttons, stop buttons etc

```html
<!DOCTYPE html>
<html lang="en">
<head>
<meta charset="utf-8">
<title>Hollow Lanterns</title>
<link href="https://fonts.googleapis.com/css2?family=Open+Sans:wght@400;600&family=Ubuntu:wght@400;500;700&display=swap" rel="stylesheet">
<style>
:root{
  --ink:#111;
  --header:#0b0b0b;
  --accent:#b2416b;
  --violet:#7a5a9e;
  --plum:#6a3b86;
  --text:#555;
  --muted:#888;
  --rule:#e2e2e2;
  --footer:#222;
  --footer-deep:#1a1a1a;
  --footer-box:#2b2b2b;
  --footer-text:#bbb;
  --white:#fff;
}
*{margin:0;padding:0;box-sizing:border-box}
html,body{width:846px;height:1200px;overflow:hidden;background:var(--white)}
body{position:relative;font-family:"Open Sans",Arial,sans-serif;color:var(--text)}
.abs{position:absolute}
.site-header{left:0;top:0;width:846px;height:70px;background:var(--header)}
.brand{left:70px;top:20px;display:flex;align-items:center;gap:8px}
.brand-dot{width:28px;height:28px;border-radius:50%;background:var(--white)}
.brand-name{font-family:"Open Sans",sans-serif;font-size:10px;letter-spacing:3px;color:var(--white);text-transform:uppercase;line-height:12px;width:90px}
.nav a{position:absolute;top:32px;font-size:8.5px;color:var(--white);text-decoration:none;white-space:nowrap}
.nav a.active{color:#e26d92}
.music{left:758px;top:24px}
.hero{left:70px;top:90px;width:708px;height:308px;background:linear-gradient(180deg,#7fb3c9 0%,#9cc4cf 55%,#5fa9b4 80%,#d8e4e6 100%)}
.hero-arrows{left:730px;top:334px;display:flex;gap:2px}
.hero-arrows span{width:17px;height:16px;background:rgba(90,90,90,.55);color:#fff;font-size:10px;text-align:center;line-height:16px}
.welcome-title{left:0;width:846px;top:417px;text-align:center;font-family:Ubuntu,sans-serif;font-weight:700;font-size:12px;color:var(--accent);letter-spacing:.3px}
.welcome-lead{left:0;width:846px;top:441px;text-align:center;font-size:12.4px;color:#444}
.feature h3{font-family:"Open Sans",sans-serif;font-weight:400;font-size:11.2px;color:var(--violet);margin-bottom:6px}
.feature p{font-family:Arial,sans-serif;font-size:7.2px;line-height:16px;color:#666;width:190px}
.feature-icon{position:absolute}
.rule{height:1px;background:var(--rule)}
.rule.dotted{background:none;border-top:1px dashed #d6d6d6}
.section-title{font-family:Ubuntu,sans-serif;font-size:12.2px;color:var(--accent);text-transform:uppercase}
.view-all{left:722px;top:594px;width:54px;height:18px;background:var(--accent);color:#fff;font-family:Ubuntu,sans-serif;font-weight:700;font-size:5.8px;text-align:center;line-height:18px}
.card{top:634px;width:168px;height:100px;background:#fff;border:1px solid #e6e6e6;box-shadow:0 4px 5px -3px rgba(0,0,0,.35)}
.card-photo{position:absolute;left:7px;top:6px;width:154px;height:89px}
.video{left:70px;top:791px;width:387px;height:162px}
.video-frame{position:absolute;left:0;top:0;width:387px;height:144px;background:linear-gradient(180deg,#8c8c86 0%,#cfd0c8 50%,#a6a49a 100%)}
.video-bar{position:absolute;left:0;top:144px;width:387px;height:18px;background:#141414;color:#ddd;font-size:6px}
.blog-post h4{font-family:"Open Sans",sans-serif;font-weight:400;font-size:8.4px;color:var(--plum)}
.blog-post p{font-family:Arial,sans-serif;font-size:6.9px;line-height:16px;color:#555;margin-top:5px;width:280px}
.blog-post time{display:block;font-size:6.9px;color:var(--muted);margin-top:2px}
.site-footer{left:0;top:982px;width:846px;height:172px;background:var(--footer)}
.footer-title{font-family:"Open Sans",sans-serif;font-weight:600;font-size:8.4px;color:#eee;text-transform:uppercase}
.footer-text{font-size:7.4px;line-height:16px;color:var(--footer-text)}
.socials{left:70px;top:1024px;display:flex;gap:17px}
.socials span{width:9px;height:9px;border-radius:50%;background:#ddd}
.post-link{font-size:8px;color:#ccc}
.post-date{font-size:7px;color:#e05c89;margin-top:4px}
.comment{left:452px;width:119px;height:43px;background:var(--footer-box);padding:9px 9px;font-size:7px;line-height:16px;color:var(--footer-text)}
.bottom-bar{left:0;top:1154px;width:846px;height:46px;background:var(--footer-deep)}
.copyright{left:70px;top:1171px;font-size:7.2px;color:#bbb}
.legal{right:70px;top:1171px;font-size:7.2px;color:#bbb}
</style>
</head>
<body>

<header class="abs site-header">
  <div class="abs brand"><span class="brand-dot"></span><span class="brand-name">Hollow Lanterns</span></div>
  <nav class="nav">
    <a class="active" style="left:316px">HOME</a>
    <a style="left:381px">ABOUT US</a>
    <a style="left:462px">SERVICES</a>
    <a style="left:538px">BLOW</a>
    <a style="left:602px">PRODUTS</a>
    <a style="left:680px">CONTACT US</a>
  </nav>
  <svg class="abs music" width="18" height="20" viewBox="0 0 18 20" aria-label="Background music">
    <path d="M6 3 L16 1 L16 14" stroke="#e8d84a" stroke-width="2.4" fill="none"/>
    <path d="M6 3 L6 16" stroke="#e8d84a" stroke-width="2.4"/>
    <ellipse cx="4" cy="16" rx="3" ry="2.4" fill="#e8d84a"/>
    <ellipse cx="14" cy="14" rx="3" ry="2.4" fill="#e8d84a"/>
  </svg>
</header>

<div class="abs hero" role="img" aria-label="Living room with a turquoise sofa, white cushions and framed pictures on a striped wall"></div>
<div class="abs hero-arrows"><span>&#8249;</span><span>&#8250;</span></div>

<h1 class="abs welcome-title">WELCOME TO OUR COMPANY</h1>
<p class="abs welcome-lead">Sed ut perspiciatis unde omnis iste natus error&nbsp; totam rem aperiam, eaque ipsa quae ab illo inventore veritatis</p>

<section class="features">
  <svg class="feature-icon" style="left:70px;top:488px" width="26" height="26" viewBox="0 0 26 26" aria-hidden="true">
    <rect x="2" y="16" width="5" height="8" fill="var(--violet)"/><rect x="9" y="11" width="5" height="13" fill="var(--violet)"/><rect x="16" y="4" width="5" height="20" fill="var(--violet)"/><rect x="0" y="24" width="24" height="1.5" fill="var(--violet)"/>
  </svg>
  <div class="abs feature" style="left:110px;top:486px"><h3>Nemo enim ipsam</h3><p>At vero eos et accusamus et iusto odio dignissimos ducimus qui blanditiis praesentium voluptatum molestias excepturi sint occaecat</p></div>

  <svg class="feature-icon" style="left:315px;top:488px" width="28" height="24" viewBox="0 0 28 24" aria-hidden="true">
    <ellipse cx="14" cy="10" rx="13" ry="9" fill="var(--violet)"/><path d="M6 16 L4 23 L12 18Z" fill="var(--violet)"/>
    <circle cx="8" cy="10" r="1.8" fill="#fff"/><circle cx="14" cy="10" r="1.8" fill="#fff"/><circle cx="20" cy="10" r="1.8" fill="#fff"/>
  </svg>
  <div class="abs feature" style="left:352px;top:486px"><h3>Nemo enim ipsam</h3><p>At vero eos et accusamus et iusto odio dignissimos ducimus qui blanditiis praesentium voluptatum molestias excepturi sint occaecat</p></div>

  <svg class="feature-icon" style="left:557px;top:490px" width="30" height="20" viewBox="0 0 30 20" aria-hidden="true">
    <path d="M1 5 L8 2 L15 6 L22 2 L29 5 L27 12 L18 19 L11 14 L3 12Z" fill="var(--violet)"/>
    <path d="M10 8 L16 12 M13 6 L19 11" stroke="#fff" stroke-width="1.2"/>
  </svg>
  <div class="abs feature" style="left:598px;top:486px"><h3>Nemo enim ipsam</h3><p>At vero eos et accusamus et iusto odio dignissimos ducimus qui blanditiis praesentium voluptatum molestias excepturi sint occaecat</p></div>
</section>

<div class="abs rule" style="left:70px;top:576px;width:707px"></div>

<h2 class="abs section-title" style="left:70px;top:597px">Latest Articles</h2>
<div class="abs view-all">VIEW ALL</div>
<div class="abs rule dotted" style="left:70px;top:628px;width:707px"></div>

<article class="abs card" style="left:70px"><div class="card-photo" role="img" aria-label="Lounge with blue sofas and a glass coffee table" style="background:linear-gradient(180deg,#b9bcc2,#6f78a8 65%,#8a8172)"></div></article>
<article class="abs card" style="left:250px"><div class="card-photo" role="img" aria-label="Person relaxing on a cream sofa with a tablet" style="background:linear-gradient(180deg,#6d655d,#bfb2a4 60%,#ece6df)"></div></article>
<article class="abs card" style="left:429px"><div class="card-photo" role="img" aria-label="Home cook preparing vegetables in a kitchen" style="background:linear-gradient(180deg,#8e8c88,#b96d6a 60%,#9a8a6a)"></div></article>
<article class="abs card" style="left:608px"><div class="card-photo" role="img" aria-label="Bright dining table set with plates and greenery" style="background:linear-gradient(180deg,#d9d7d1,#e9e6df 55%,#a99786)"></div></article>

<div class="abs rule dotted" style="left:70px;top:742px;width:707px"></div>

<h2 class="abs section-title" style="left:70px;top:760px">Our Video</h2>
<div class="abs video">
  <div class="video-frame" role="img" aria-label="Video still of a living room with striped armchairs and sofa by tall windows"></div>
  <div class="video-bar">
    <div style="position:absolute;left:0;top:0;width:387px;height:2px;background:#555"></div>
    <div style="position:absolute;left:0;top:0;width:14px;height:2px;background:#d12b2b"></div>
    <svg style="position:absolute;left:12px;top:6px" width="8" height="8" viewBox="0 0 8 8"><rect x="1" y="0" width="2" height="8" fill="#ddd"/><rect x="5" y="0" width="2" height="8" fill="#ddd"/></svg>
    <svg style="position:absolute;left:37px;top:6px" width="12" height="8" viewBox="0 0 12 8"><path d="M0 2.5h2.5L5.5 0v8L2.5 5.5H0Z" fill="#ddd"/><path d="M8 2l3 4M11 2l-3 4" stroke="#ddd" stroke-width="1"/></svg>
    <span style="position:absolute;left:60px;top:5px;color:#fff">0:03 <span style="color:#999">/ 1:35</span></span>
    <svg style="position:absolute;left:319px;top:5px" width="62" height="9" viewBox="0 0 62 9" fill="none" stroke="#ddd" stroke-width="1.2">
      <circle cx="4" cy="4.5" r="3" fill="#ddd"/>
      <circle cx="19" cy="4.5" r="2.5"/><path d="M19 0v2M19 7v2M14.5 4.5h2M21.5 4.5h2"/>
      <rect x="31" y="1.5" width="9" height="6"/>
      <path d="M48 1h-2v2M58 1h2v2M48 8h-2v-2M58 8h2v-2"/>
    </svg>
  </div>
</div>

<h2 class="abs section-title" style="left:491px;top:762px">Blog</h2>
<div class="abs" style="left:761px;top:764px;font-size:9px;color:#aaa">&#8249; &#8250;</div>

<article class="abs blog-post" style="left:491px;top:790px">
  <h4>At vero eos et accusamus et iusto ....</h4>
  <p>Sed ut perspiciatis unde omnis iste natus error sit voluptatem accusantium&nbsp; illo inventore veritatis et quasi architecto beatae...</p>
  <time>Posted on 14/01/2015&nbsp;&nbsp; 8:28:58 AM</time>
</article>
<div class="abs rule" style="left:491px;top:867px;width:251px"></div>
<article class="abs blog-post" style="left:491px;top:880px">
  <h4>At vero eos et accusamus et iusto ....</h4>
  <p>Sed ut perspiciatis unde omnis iste natus error sit voluptatem accusantium&nbsp; illo inventore veritatis et quasi architecto beatae...</p>
  <time>Posted on 14/01/2015&nbsp;&nbsp; 8:28:58 AM</time>
</article>

<footer class="abs site-footer"></footer>
<h3 class="abs footer-title" style="left:71px;top:995px">Keep in touch</h3>
<div class="abs socials"><span></span><span></span><span></span><span></span><span></span><span></span></div>
<p class="abs footer-text" style="left:71px;top:1046px;width:200px">Lorem ipsum dolor sit amet, consectetur adipiscing elit. Maecenas non magna. Mattis purus sit amet fermentum.</p>
<p class="abs footer-text" style="left:71px;top:1109px;width:200px">Maecenas sed diam eget risus varius blandit sit amet non magna.</p>

<h3 class="abs footer-title" style="left:292px;top:995px">Recent posts</h3>
<div class="abs" style="left:292px;top:1024px"><div class="post-link">Another Standard Post Type</div><div class="post-date">Jan 15, 2015</div></div>
<div class="abs" style="left:292px;top:1067px"><div class="post-link">Another Standard Post Type</div><div class="post-date">Jan 15, 2015</div></div>
<div class="abs" style="left:292px;top:1112px"><div class="post-link">Another Standard Post Type</div><div class="post-date">Jan 15, 2015</div></div>

<h3 class="abs footer-title" style="left:450px;top:995px">Recent comments</h3>
<div class="abs comment" style="top:1023px">Lorem ipsum dolor sit amet, adipiscing</div>
<div class="abs comment" style="top:1086px">Lorem ipsum dolor sit amet, adipiscing</div>

<h3 class="abs footer-title" style="left:619px;top:995px">Latest tweets</h3>
<span class="abs" style="left:620px;top:1024px;width:9px;height:9px;border-radius:50%;background:#888"></span>
<p class="abs footer-text" style="left:638px;top:1019px;width:145px">RT @brightmarket: Attending the Indonesian Brightmarket Authors National Meetup - http://lnk.example/Q7mRtW2pLs http://lnk.example/Hk3vBn8Zc December 15, 2014 - 1:08 am</p>

<div class="abs bottom-bar"></div>
<p class="abs copyright">©2015 hollow lanterns all right reseved.</p>
<p class="abs legal">Home&nbsp; /&nbsp; Terms of Use &amp; Privacy Policy&nbsp; /&nbsp; Contact us</p>

</body>
</html>
```